Email Banner (LumenBriefs)

We require an email banner for our email promotions sent to prospect clients. The banner needs to contain the wording LumenBriefs and use the same colour scheme as the logos attached.

This is for B2B professional's so needs to look like a place you would come to read technology articles.

```html
<!DOCTYPE html>
<html lang="en">
<head>
<meta charset="utf-8">
<title>LumenBriefs Email Banner</title>
<link rel="stylesheet" href="https://fonts.googleapis.com/css2?family=Outfit:wght@500&family=Arimo:wght@400&display=swap">
<style>
  :root {
    --page-bg: #dededc;
    --banner-bg: #ffffff;
    --ink: #0c1527;
    --text-dark: #1a1a1a;
    --green-deep: #009640;
    --green-light: #86c22a;
    --blue: #0a8fdc;
    --teal: #0098b8;
    --white: #ffffff;
  }
  html, body {
    margin: 0;
    width: 1200px;
    height: 1200px;
    overflow: hidden;
    background: var(--page-bg);
  }
  .canvas {
    position: relative;
    width: 1200px;
    height: 1200px;
  }
  .email-banner {
    position: absolute;
    left: 92px;
    top: 426px;
    width: 992px;
    height: 371px;
    display: block;
  }
  .brand-name {
    font-family: "Outfit", sans-serif;
    font-weight: 500;
    font-size: 104px;
    fill: var(--ink);
  }
  .social-label {
    font-family: "Arimo", sans-serif;
    font-size: 31px;
    fill: var(--text-dark);
  }
  .contact-line {
    font-family: "Arimo", sans-serif;
    font-size: 29px;
    fill: var(--white);
  }
</style>
</head>
<body>
<div class="canvas">
  <svg class="email-banner" viewBox="0 0 1597 597" xmlns="http://www.w3.org/2000/svg" role="img" aria-label="LumenBriefs email banner">
    <defs>
      <linearGradient id="panelGradient" x1="0" y1="0" x2="1" y2="0">
        <stop offset="0" stop-color="var(--green-deep)"/>
        <stop offset="1" stop-color="var(--teal)"/>
      </linearGradient>
      <radialGradient id="accentGradient" cx="0.3" cy="0.7" r="0.7">
        <stop offset="0" stop-color="var(--green-light)" stop-opacity="0.15"/>
        <stop offset="0.6" stop-color="var(--green-light)" stop-opacity="0.45"/>
        <stop offset="1" stop-color="var(--blue)" stop-opacity="0.7"/>
      </radialGradient>
      <radialGradient id="cornerGradient" cx="0.5" cy="0.5" r="0.5">
        <stop offset="0" stop-color="var(--white)" stop-opacity="0.05"/>
        <stop offset="1" stop-color="var(--white)" stop-opacity="0.35"/>
      </radialGradient>
      <clipPath id="bannerClip">
        <rect x="0" y="0" width="1597" height="597"/>
      </clipPath>
    </defs>

    <rect class="banner-bg" x="0" y="0" width="1597" height="597" fill="var(--banner-bg)"/>

    <g clip-path="url(#bannerClip)">
      <circle class="contact-panel" cx="1400" cy="319" r="397" fill="url(#panelGradient)"/>
      <circle class="corner-accent" cx="1575" cy="61" r="183" fill="url(#cornerGradient)" role="img" aria-label="Decorative ring ornament area"/>
      <circle class="accent-area" cx="91" cy="504" r="240" fill="url(#accentGradient)" role="img" aria-label="Decorative ring ornament area in blue and green"/>
    </g>

    <g class="brand">
      <rect class="brand-mark" x="92" y="112" width="74" height="74" fill="var(--blue)"/>
      <text class="brand-name" x="204" y="186">LumenBriefs.io</text>
    </g>

    <g class="social-links">
      <rect class="social-icon" x="508" y="427" width="38" height="38" rx="6" fill="var(--text-dark)"/>
      <text class="social-label" x="527" y="504" text-anchor="middle">Picshare</text>

      <rect class="social-icon" x="682" y="427" width="38" height="38" rx="6" fill="var(--text-dark)"/>
      <text class="social-label" x="701" y="504" text-anchor="middle">Kinbook</text>

      <circle class="social-icon" cx="850" cy="446" r="19" fill="var(--text-dark)"/>
      <text class="social-label" x="850" y="504" text-anchor="middle">Chirpnet</text>
    </g>

    <g class="contact-details">
      <text class="contact-line" x="1128" y="377">Contact :</text>
      <text class="contact-line" x="1128" y="411">Email:@lumenmail.com</text>
      <text class="contact-line" x="1130" y="460">Company Name :</text>
      <text class="contact-line" x="1130" y="491">Office Name :</text>
      <text class="contact-line" x="1130" y="522">City Name :</text>
    </g>
  </svg>
</div>
</body>
</html>
```